Plastering (solid plastering) business card design

We need a business card for a a small plastering business based in Perth Western Australia. We are a small team that provides a service in solid plastering specialising in float, white set and sand finish. We would like to see a clean business card with our name "Brightline Plastering" being the focus of the card and maybe incorporated into a logo. We don't have a logo at the moment so we would like to see some cards that may provide us with our future logo.

Industry/Entity Type

Business

Contact Information for Business Card

Brightline Plastering

Solid Plastering Specialists

Ph: Corey 0417683091
Ph: Liam 0468120357

Requirements
Should not have
• The design should not have Drywall incorporated into the card. In perth W.A. Plastering in different to someone that puts up Plyvane. We use sand, cement, lime and hardwall plaster.

```html
<!DOCTYPE html>
<html lang="en">
<head>
<meta charset="utf-8">
<title>Brightline Plastering – Business Card</title>
<link rel="stylesheet" href="https://fonts.googleapis.com/css2?family=Roboto+Condensed:wght@700&family=Roboto:wght@500;700&display=swap">
<style>
  :root {
    --page-bg: #e6e4e0;
    --card-white: #f5f5f4;
    --swoosh-grey: #858585;
    --title-white: #ffffff;
    --tagline-yellow: #f2ee1c;
    --brand-blue: #3f5b91;
    --name-red: #8e1c1c;
    --phone-green: #1f8a3c;
    --text-black: #111111;
  }
  * { margin: 0; padding: 0; box-sizing: border-box; }
  html, body {
    width: 1200px;
    height: 1200px;
    overflow: hidden;
    background: var(--page-bg);
  }
  .canvas {
    position: relative;
    width: 1200px;
    height: 1200px;
  }
  .card {
    position: absolute;
    left: 80px;
    top: 281px;
    width: 1040px;
    height: 638px;
    background: var(--card-white);
    overflow: hidden;
    box-shadow: 0 2px 10px rgba(0,0,0,0.12);
  }
  .card__swoosh {
    position: absolute;
    inset: 0;
    width: 100%;
    height: 100%;
  }
  .card__swoosh path { fill: var(--swoosh-grey); }

  .headline {
    position: absolute;
    left: 56px;
    top: 92px;
    width: 510px;
    text-align: center;
  }
  .headline__name {
    font-family: "Roboto Condensed", "Arial Narrow", sans-serif;
    font-weight: 700;
    font-size: 45px;
    line-height: 1;
    color: var(--title-white);
    letter-spacing: 0.2px;
    text-transform: uppercase;
  }
  .headline__tagline {
    margin-top: 8px;
    font-family: "Roboto Condensed", "Arial Narrow", sans-serif;
    font-weight: 700;
    font-size: 21px;
    line-height: 1;
    color: var(--tagline-yellow);
    text-transform: uppercase;
  }

  .brand-mark {
    position: absolute;
    left: 662px;
    top: 70px;
    width: 320px;
    font-family: "Roboto Condensed", "Arial Narrow", sans-serif;
    font-weight: 700;
    font-size: 48px;
    line-height: 1.02;
    color: var(--brand-blue);
    text-transform: uppercase;
  }

  .contacts {
    position: absolute;
    left: 66px;
    top: 368px;
    width: 260px;
  }
  .contact + .contact { margin-top: 26px; }
  .contact__name {
    font-family: "Roboto", Arial, sans-serif;
    font-weight: 500;
    font-size: 30px;
    line-height: 1;
    color: var(--name-red);
    padding-bottom: 6px;
    border-bottom: 2px solid var(--text-black);
  }
  .contact__phone {
    display: flex;
    align-items: center;
    gap: 9px;
    margin-top: 10px;
    font-family: "Roboto", Arial, sans-serif;
    font-weight: 700;
    font-size: 28px;
    line-height: 1;
    color: var(--text-black);
    letter-spacing: 0.4px;
  }
  .contact__icon {
    width: 28px;
    height: 24px;
    flex: none;
  }
  .contact__icon path, .contact__icon circle { fill: var(--phone-green); }
  .contact__icon .dial { fill: var(--card-white); }
</style>
</head>
<body>
<main class="canvas">
  <article class="card">
    <svg class="card__swoosh" viewBox="0 0 713 438" preserveAspectRatio="none" aria-hidden="true">
      <path d="M0,34 C140,6 330,10 390,30 C430,44 440,70 435,120 C430,200 440,270 520,330 C600,385 660,400 713,405 L713,428 C560,405 360,335 318,262 C300,230 305,200 280,180 C220,150 80,150 0,152 Z"/>
    </svg>

    <header class="headline">
      <h1 class="headline__name">Brightline Plastering</h1>
      <p class="headline__tagline">Solid Plastering Specialists</p>
    </header>

    <div class="brand-mark">Brightline<br>Plastering</div>

    <section class="contacts">
      <div class="contact">
        <p class="contact__name">Liam</p>
        <p class="contact__phone">
          <svg class="contact__icon" viewBox="0 0 28 24" aria-hidden="true">
            <path d="M2,8 C2,3 8,1 14,1 C20,1 26,3 26,8 L26,10 L20,10 L20,7 C18,6 10,6 8,7 L8,10 L2,10 Z"/>
            <path d="M7,11 L21,11 L25,22 L3,22 Z"/>
            <circle class="dial" cx="14" cy="16" r="4"/>
            <circle cx="14" cy="16" r="1.6"/>
          </svg>
          <span>0468120357</span>
        </p>
      </div>
      <div class="contact">
        <p class="contact__name">Corey</p>
        <p class="contact__phone">
          <svg class="contact__icon" viewBox="0 0 28 24" aria-hidden="true">
            <path d="M2,8 C2,3 8,1 14,1 C20,1 26,3 26,8 L26,10 L20,10 L20,7 C18,6 10,6 8,7 L8,10 L2,10 Z"/>
            <path d="M7,11 L21,11 L25,22 L3,22 Z"/>
            <circle class="dial" cx="14" cy="16" r="4"/>
            <circle cx="14" cy="16" r="1.6"/>
          </svg>
          <span>0417683091</span>
        </p>
      </div>
    </section>
  </article>
</main>
</body>
</html>
```